Business Card Design for new social media business

I am looking for a new professional business card design for an exciting new company which is based on providing members with experiences of others to benefit their choice of places to visit for restaurants, bars, clubs, national monument, tourist sights, hotels and so forth.
Updates

Please submit designs as I will choose to commit the funds depending on designs.

Target Market(s)

Business Managers as well as directors alongside owners

Industry/Entity Type

Business

Requirements
Must have
• Logo design and symbols
Nice to have
• Logo / Symbol on the back of the business card and possibly the logo as if embedded/embossed on the business card.

```html
<!DOCTYPE html>
<html lang="en">
<head>
<meta charset="utf-8">
<title>ViewNest Business Card</title>
<link href="https://fonts.googleapis.com/css2?family=Barlow:wght@400;700&display=swap" rel="stylesheet">
<style>
  :root {
    --bg: #e9e9eb;
    --card: #ffffff;
    --edge: #f29a1c;
    --brand-blue: #2b55b0;
    --accent-orange: #f07d1a;
    --icon-blue: #2f63c4;
    --text-dark: #3a3a3a;
    --text-mid: #555a60;
    --map-light: #cfe2fa;
    --map-mid: #a9cdf5;
  }
  * { box-sizing: border-box; margin: 0; padding: 0; }
  html, body { width: 1200px; height: 1000px; overflow: hidden; }
  body {
    background: var(--bg);
    font-family: "Barlow", Arial, sans-serif;
    position: relative;
  }
  .card {
    position: absolute;
    width: 520px;
    height: 300px;
    background: var(--card);
    border-bottom: 5px solid var(--edge);
    box-shadow: 0 10px 28px rgba(0,0,0,0.12);
    overflow: hidden;
  }
  .card--front { left: 40px; top: 350px; }
  .card--back { left: 640px; top: 350px; }

  .brand {
    display: flex;
    align-items: center;
    gap: 10px;
    font-weight: 700;
    color: var(--brand-blue);
    letter-spacing: -0.5px;
  }
  .brand__dot {
    border-radius: 50%;
    background: var(--accent-orange);
    flex: none;
  }
  .card--front .brand {
    position: absolute;
    left: 44px; top: 52px;
    font-size: 42px;
  }
  .card--front .brand__dot { width: 34px; height: 34px; }

  .holder-name {
    position: absolute;
    left: 150px; top: 180px;
    font-size: 22px;
    color: var(--text-dark);
    letter-spacing: 0.5px;
  }
  .divider {
    position: absolute;
    left: 310px; top: 90px;
    width: 1.5px; height: 115px;
    background: var(--icon-blue);
  }
  .contact {
    position: absolute;
    left: 330px; top: 96px;
    list-style: none;
  }
  .contact__item {
    display: flex;
    align-items: center;
    gap: 12px;
    font-size: 15px;
    color: var(--text-mid);
    height: 28px;
  }
  .contact__icon { width: 14px; height: 14px; flex: none; }

  .map-area {
    position: absolute;
    inset: 0;
    background: linear-gradient(135deg, var(--map-light) 0%, var(--map-mid) 100%);
    opacity: 0.75;
  }
  .card--back .brand {
    position: absolute;
    left: 230px; top: 160px;
    font-size: 40px;
  }
  .card--back .brand__dot { width: 32px; height: 32px; }
</style>
</head>
<body>
  <section class="card card--front" aria-label="Business card front">
    <div class="brand">
      <span class="brand__dot"></span>
      <span class="brand__name">ViewNest</span>
    </div>
    <p class="holder-name">Ravin Mehta</p>
    <div class="divider"></div>
    <ul class="contact">
      <li class="contact__item">
        <svg class="contact__icon" viewBox="0 0 24 24" aria-hidden="true"><path fill="var(--icon-blue)" d="M6.6 10.8a15.1 15.1 0 0 0 6.6 6.6l2.2-2.2c.3-.3.7-.4 1-.2 1.1.4 2.3.6 3.6.6.6 0 1 .4 1 1V20c0 .6-.4 1-1 1A17 17 0 0 1 3 4c0-.6.4-1 1-1h3.5c.6 0 1 .4 1 1 0 1.3.2 2.5.6 3.6.1.3 0 .7-.2 1z"/></svg>
        <span>555.012.3478</span>
      </li>
      <li class="contact__item">
        <svg class="contact__icon" viewBox="0 0 24 24" aria-hidden="true"><rect x="2" y="5" width="20" height="14" fill="var(--icon-blue)"/><path d="M2 5l10 8 10-8" fill="none" stroke="#fff" stroke-width="2"/></svg>
        <span>rmehta@viewnest.com</span>
      </li>
      <li class="contact__item">
        <svg class="contact__icon" viewBox="0 0 24 24" aria-hidden="true"><circle cx="12" cy="12" r="10" fill="var(--icon-blue)"/><path d="M2 12h20M12 2c3 3 3 17 0 20M12 2c-3 3-3 17 0 20" fill="none" stroke="#fff" stroke-width="1.5"/></svg>
        <span>www.viewnest.com</span>
      </li>
    </ul>
  </section>

  <section class="card card--back" aria-label="Business card back">
    <div class="map-area" role="img" aria-label="Pixelated world map in light blue squares"></div>
    <div class="brand">
      <span class="brand__dot"></span>
      <span class="brand__name">ViewNest</span>
    </div>
  </section>
</body>
</html>
```